Web Design for an Online Dating Web Site

We need an uncoded web design for a new online dating web site called zMatchy.net. Simplicity and boldness are the key factors in the successful design.
Please look at the requirements document attached for details.
Updates
Dear all,
Please AVOID USING A PICTURE OF A HAPPY COUPLE ON THE HOME PAGE of the site. We highly want to move away from this space as it makes our web site just like another dating web site.
We like something simple with web 2.0 look and feel. The examples in the Requirements Document are exactly the design we are after.
Regards
Tarn
Industry/Entity Type
Dating
Look and feel
Each slider illustrates characteristics of the customer's brand and the style your logo design should communicate.

```html
<!DOCTYPE html>
<html lang="en">
<head>
<meta charset="utf-8">
<title>zMatchy.net</title>
<link href="https://fonts.googleapis.com/css2?family=Arimo:wght@400;700&family=Nunito:wght@700;800&display=swap" rel="stylesheet">
<style>
:root{
  --pink:#e0288a;
  --pink-dark:#cc1272;
  --pink-light:#f07ab8;
  --teal:#4bc3d6;
  --teal-text:#4fbcd2;
  --teal-pale:#a8eef4;
  --teal-faint:#a5e6ef;
  --page:#ececec;
  --white:#ffffff;
  --grey:#7a7a7a;
  --dark:#333333;
}
*{margin:0;padding:0;box-sizing:border-box}
html,body{width:1200px;height:1069px;overflow:hidden}
body{position:relative;background:var(--page);font-family:"Arimo",Arial,sans-serif;color:var(--dark)}
.abs{position:absolute}
.column{left:245px;width:708px;background:var(--white)}
.header{top:0;height:115px;box-shadow:0 0 14px rgba(0,0,0,.12)}
.brand{left:470px;top:28px;display:flex;align-items:center;gap:8px}
.brand-name{font-family:"Nunito",sans-serif;font-weight:800;font-size:52px;color:var(--pink);line-height:1}
.brand-dot{width:14px;height:14px;border-radius:50%;background:var(--pink)}
.brand-url{left:633px;top:74px;font-size:11px;color:var(--grey)}
.nav{left:245px;top:115px;width:712px;height:57px;background:linear-gradient(var(--pink),var(--pink-dark));display:flex}
.nav-item{width:103px;height:57px;display:flex;flex-direction:column;align-items:center;justify-content:flex-end;padding-bottom:6px;color:var(--white);font-size:11px;border-right:1px dotted rgba(255,255,255,.45)}
.nav-item svg{margin-bottom:4px}
.nav-item.active{background:var(--white);color:var(--pink);font-weight:700;position:relative}
.nav-item.active::after{content:"";position:absolute;bottom:0;left:47px;border:5px solid transparent;border-bottom-color:var(--pink)}
.login{position:relative;width:172px;color:var(--white);font-size:10px}
.login label{position:absolute;left:14px}
.field{position:absolute;left:63px;width:80px;height:13px;border-radius:7px;background:var(--pink-light)}
.login-btn{position:absolute;left:100px;top:37px;width:42px;height:15px;border-radius:3px;background:var(--white);color:var(--pink);font-size:10px;text-align:center;line-height:15px}
.check{position:absolute;left:17px;top:39px;width:8px;height:8px;background:var(--white)}
.or{position:absolute;left:155px;top:14px;width:32px;height:32px;border:1px solid rgba(255,255,255,.7);border-radius:50%;text-align:center;line-height:30px;font-size:12px}
.social-sq{width:18px;height:18px;border-radius:3px;background:rgba(255,255,255,.85)}
.more{left:905px;top:146px;width:35px;height:17px;border-radius:2px;background:var(--white);color:var(--pink);font-size:8px;font-weight:700;text-align:center;line-height:17px}
.hero{left:0;top:172px;width:1200px;height:320px;background:linear-gradient(#ececec 0%,#fff 15%,#fff 55%,#e6e6e6 100%)}
.arrow{top:305px;width:46px;height:45px;background:var(--pink);display:flex;align-items:center;justify-content:center}
.arrow.left{left:0;border-radius:0 8px 8px 0}
.arrow.right{left:1154px;border-radius:8px 0 0 8px}
.hero-art{left:322px;top:213px;width:236px;height:270px;background:linear-gradient(90deg,#e482c8 0 50%,#6fc5d4 50% 100%);border-radius:40px;opacity:.85}
.hero-title{left:652px;top:258px;font-size:30px;font-weight:700;color:var(--pink)}
.hero-sub{left:652px;top:294px;font-size:11px;font-weight:700;color:var(--grey)}
.hero-body{left:652px;top:321px;font-size:15px;font-weight:700;color:var(--pink);line-height:19px}
.cta{left:687px;top:383px;width:188px;height:63px;border-radius:18px;border:4px solid #a9a9a9;background:linear-gradient(#f04ea5,var(--pink-dark));color:var(--white);font-size:25px;text-align:center;line-height:55px}
.content{top:492px;height:331px;box-shadow:0 0 14px rgba(0,0,0,.15)}
.video{left:269px;top:514px;width:420px;height:256px;background:linear-gradient(#3f4a58 0%,#6c7a88 45%,#2c3438 100%)}
.play{left:428px;top:578px}
.controls{left:269px;top:770px;width:420px;height:23px;background:linear-gradient(#eee,#cfcfcf);box-shadow:0 3px 6px rgba(0,0,0,.2)}
.bar{top:779px;height:6px;border-radius:3px}
.time{left:524px;top:777px;font-size:9px;color:#555}
.divider{left:713px;top:520px;height:270px;border-left:1px dotted #aaa}
.posts-title{left:736px;top:527px;font-size:16px;font-weight:700;color:var(--teal-text)}
.thumb{left:737px;width:44px;height:44px;background:#6a6a6a;border:3px solid #ddd;border-radius:3px}
.post-title{left:789px;width:150px;font-size:12px;color:var(--teal-text);line-height:14px}
.post-meta{left:789px;font-size:7px;color:#555;font-family:Georgia,serif}
.footer{left:0;top:823px;width:1200px;height:246px;background:var(--teal)}
.footer-rule{left:0;top:829px;width:1200px;border-top:1px dashed rgba(255,255,255,.5)}
.foot-head{top:845px;font-size:18px;font-weight:700;color:var(--teal-faint);padding-bottom:9px;border-bottom:1px solid rgba(255,255,255,.7)}
.foot-links{left:247px;top:887px;list-style:none;font-size:10px;font-weight:700;color:var(--white);line-height:12px}
.input{left:495px;width:159px;height:20px;background:var(--teal-pale);border-radius:2px;color:var(--white);font-size:9px;padding:5px 7px}
.send{left:495px;top:1029px;width:96px;height:20px;background:var(--dark);color:var(--white);font-size:9px;font-weight:700;text-align:center;line-height:20px;border-radius:2px}
.foot-brand{left:743px;top:845px;display:flex;align-items:center;gap:5px}
.foot-brand span{font-family:"Nunito",sans-serif;font-weight:800;font-size:24px;color:var(--white)}
.foot-brand i{width:8px;height:8px;border-radius:50%;background:var(--white)}
.icon-sq{width:15px;height:15px;border-radius:2px;background:rgba(255,255,255,.85)}
.share{height:14px;background:#dfeff7;border:1px solid #a9c4d6;font-size:8px;color:#3a5a80;line-height:12px;padding:0 4px}
</style>
</head>
<body>

<div class="abs column header"></div>
<div class="abs brand"><span class="brand-name">zMatchy</span><span class="brand-dot"></span></div>
<div class="abs brand-url">zmatchy.net</div>

<nav class="abs nav">
  <div class="nav-item"><svg width="28" height="26" viewBox="0 0 28 26"><path d="M7 9a7 7 0 1 1 10 6c-2 1-3 2-3 4" fill="none" stroke="#fff" stroke-width="4" stroke-linecap="round"/><circle cx="21" cy="22" r="3" fill="#fff"/></svg>Why ?</div>
  <div class="nav-item active"><svg width="30" height="28" viewBox="0 0 30 28"><circle cx="11" cy="11" r="7" fill="none" stroke="#e0288a" stroke-width="5" stroke-dasharray="3 2"/><circle cx="22" cy="21" r="5" fill="none" stroke="#e0288a" stroke-width="4" stroke-dasharray="2.5 1.5"/></svg>How It Works ?</div>
  <div class="nav-item"><svg width="30" height="28" viewBox="0 0 30 28"><rect x="3" y="5" width="18" height="20" fill="none" stroke="#fff" stroke-width="2.5"/><path d="M10 18 24 3l3 3-14 15-4 1z" fill="#fff"/></svg>Sign Up</div>
  <div class="nav-item"><svg width="30" height="28" viewBox="0 0 30 28"><circle cx="15" cy="14" r="13" fill="#fff"/><path d="M9 14l6-6M12 19l9-9" stroke="#e0288a" stroke-width="3" stroke-linecap="round"/></svg>Our Blog</div>
  <div class="login">
    <label style="top:5px">Username</label><div class="field" style="top:4px"></div>
    <label style="top:21px">Password</label><div class="field" style="top:20px"></div>
    <div class="check"></div><label style="left:29px;top:37px">Remember me</label>
    <div class="login-btn">Login</div>
    <div class="or">OR</div>
  </div>
</nav>
<div class="abs social-sq" style="left:857px;top:123px"></div>
<div class="abs social-sq" style="left:881px;top:123px"></div>
<div class="abs social-sq" style="left:905px;top:123px"></div>
<div class="abs social-sq" style="left:857px;top:146px"></div>
<div class="abs social-sq" style="left:881px;top:146px"></div>
<div class="abs more">MORE</div>

<section class="abs hero"></section>
<div class="abs arrow left"><svg width="20" height="26" viewBox="0 0 20 26"><path d="M15 3 5 13l10 10" fill="none" stroke="#fff" stroke-width="5"/></svg></div>
<div class="abs arrow right"><svg width="20" height="26" viewBox="0 0 20 26"><path d="M5 3l10 10L5 23" fill="none" stroke="#fff" stroke-width="5"/></svg></div>
<div class="abs hero-art" role="img" aria-label="Illustration of two cheerful figures, one pink and one blue, with hearts on their chests"></div>
<h1 class="abs hero-title">Lorem Ipsum</h1>
<p class="abs hero-sub">LOREM IPSUM DOLOR SIT AMET</p>
<p class="abs hero-body">Lorem ipsum dolor sit amet,<br>consectetur adipiscing elit. Maecenas.</p>
<div class="abs cta">SIGN UP</div>

<main class="abs column content"></main>
<div class="abs video" role="img" aria-label="Video still of a couple on a beach at dusk"></div>
<svg class="abs play" width="113" height="113" viewBox="0 0 113 113"><circle cx="56.5" cy="56.5" r="52" fill="none" stroke="rgba(255,255,255,.55)" stroke-width="7"/><path d="M44 32v50l40-25z" fill="rgba(255,255,255,.55)"/></svg>
<div class="abs controls"></div>
<svg class="abs" style="left:279px;top:775px" width="12" height="13"><path d="M1 1v11l10-5.5z" fill="#555"/></svg>
<div class="abs bar" style="left:307px;width:210px;background:#555"></div>
<div class="abs bar" style="left:307px;width:102px;background:#e43a4a"></div>
<div class="abs" style="left:403px;top:776px;width:12px;height:12px;border-radius:50%;background:#eee;border:1px solid #888"></div>
<div class="abs time">3.47 / 9.29</div>
<svg class="abs" style="left:580px;top:776px" width="14" height="12"><path d="M1 4h3l5-4v12L4 8H1z" fill="#555"/></svg>
<div class="abs bar" style="left:598px;width:52px;background:#555"></div>
<div class="abs" style="left:667px;top:776px;width:11px;height:11px;border:2px solid #555"></div>

<div class="abs divider"></div>
<h2 class="abs posts-title">Recent Posts</h2>
<div class="abs thumb" style="top:563px" role="img" aria-label="Post thumbnail photo"></div>
<div class="abs post-title" style="top:562px">Lorem Ipsum Dolor</div>
<div class="abs post-meta" style="top:583px">OCT 15, 2011 | 1 COMMENT | READ</div>
<div class="abs thumb" style="top:634px" role="img" aria-label="Post thumbnail photo"></div>
<div class="abs post-title" style="top:633px">Consectetur adipiscing elit</div>
<div class="abs post-meta" style="top:654px">OCT 15, 2011 | 1 COMMENT | READ</div>
<div class="abs thumb" style="top:706px" role="img" aria-label="Post thumbnail photo"></div>
<div class="abs post-title" style="top:704px">Morbi fringilla scelerisque ligula, eu sagittis diam interdum laoreet</div>
<div class="abs post-meta" style="top:756px">OCT 15, 2011 | 1 COMMENT | READ</div>

<footer class="abs footer"></footer>
<div class="abs footer-rule"></div>
<h3 class="abs foot-head" style="left:246px;width:212px">Read More</h3>
<ul class="abs foot-links"><li>Why zMatchy</li><li>How it works</li><li>Sign Up</li><li>Login</li><li>About Us</li></ul>
<h3 class="abs foot-head" style="left:495px;width:211px">Let’s Talk</h3>
<div class="abs input" style="top:887px">Name</div>
<div class="abs input" style="top:913px">Email</div>
<div class="abs input" style="top:938px;width:205px;height:84px">Comments</div>
<div class="abs send">Send the message</div>
<div class="abs foot-head" style="left:743px;width:210px;height:30px"></div>
<div class="abs foot-brand"><span>zMatchy</span><i></i></div>
<div class="abs icon-sq" style="left:744px;top:890px"></div>
<div class="abs icon-sq" style="left:763px;top:890px"></div>
<div class="abs icon-sq" style="left:782px;top:890px"></div>
<div class="abs icon-sq" style="left:801px;top:890px"></div>
<div class="abs icon-sq" style="left:831px;top:890px"></div>
<div class="abs icon-sq" style="left:744px;top:909px"></div>
<div class="abs icon-sq" style="left:763px;top:909px"></div>
<div class="abs icon-sq" style="left:782px;top:909px"></div>
<div class="abs icon-sq" style="left:801px;top:909px"></div>
<div class="abs share" style="left:858px;top:890px;width:50px">Post</div>
<div class="abs share" style="left:911px;top:890px;background:#fff">6,314</div>
<div class="abs share" style="left:858px;top:909px;width:44px;background:#4a6aa5;color:#fff;border-color:#4a6aa5">Share</div>
<div class="abs share" style="left:905px;top:909px;background:#fff">377</div>

</body>
</html>
```